Systems and Technology Consultants - Website

Design & Build a website for a new company which operates in the Systems and Technology space for Transportation, Government and Commercial sectors.

Overall design should be minimalist in nature.
Should also have a feed that provides news and event updates on the main page.
Logo has already been awarded and should be incorporated into the site.

We like the overall layout, functionality and simplicity of the below sites. Submitted designs could be similar to or a combination of the aspects on these sites, or perhaps a whole different concept - we are open to new ideas.
Vortrane.com
Merp.it

Update 1 Dated 27 May 2014

All I am moving away from the Merp.it website and would like it to be more aligned with Vortrane.com not only in layout but in functionality. I will be extending the deadline of this design brief for two weeks to incorporate additional requirements and will add addtional funding to the project.

Apologies for not having more information available to provide but with so many submissions its getting confusing.

Thanks Dermot
Updates

Please note that the brief has been updated and the deadline has been extended.

Important: We will need two language versions of the website, English and Arabic; the website is hosted on HostPeak

Hello All, Thank you for your submissions. We have narrowed it down to the final 6 designers and I just wanted to take a moment and provide a bit of feedback regarding the concepts that we like and the modifications we are looking for. First, let me mention some of the design functions we like. - At the top of the homepage we really like the "region" or "language" tab so that the website can be viewed in both English and Arabic. - We like the homepage to have clear color variation so that the different sections of the homepage are distinct. Additionally, we like the bottom portion of the homepage to be in red. We feel that draws attention to our contact information. Again, we would like the colors to integrate black, gray-scale, red, etc. - Having a search tab at the top of the home page, or integrated into the main image, so that the site is easy to navigate. - We especially like the main image to have the scrolling tabs at the bottom so it is easy to browse the services offered (Consultancy, Solutions Architecture, Masters Systems Integration, Independent Design Review). - In regards to the services offered tab we really like the idea that a few people presented that have the outside of our logo with an icon in the middle of consultancy, solutions, etc., etc. Secondly, as mentioned in our brief we really enjoy the design of vortrane site. Specially, we enjoy the strong iconic images they use, the way the tabs at the top scroll easily, and contact us page that generates an email. Lastly, I've included some photos of the concept we have been working on. What we are trying to demonstrate is how our company offers a range of services that are essentially linked together. We provide individual services that when combined present the full service package. We would like this concept to be integrated into the over concept of our website. Please feel free to ask for clarification of any of the above points or contact us if you have any additional questions. We appreciate all of your hard work and are very excited to see the updated designs. Best, Miriam Dowbrook Plenvaro Senior Program Manager miriam.dowbrook@plenvaro-mail.com

Industry/Entity Type

Government

Font styles to use
Serif
Sans Serif

Requirements
Must have
• Must work on/adapt to various/mobile devices (responsive)
Must be simple and straightforward
Colors should be in line/matching with logo
2 language versions: English and Arabic (no Thai)
Services should be the first group/row of items after/below the main image
Note: the website will be hosted by hostpeak
Nice to have
• Submit feedback form
What's New section
The banner at the bottom of the site should not be too large; we would like a narrow one more
It would be nice if the header/top banner (with Home, About, etc. tabs) could stay in place as you scroll down (like Vortrane and Chatterly)
We will likely only use one image with a Company slogan on the Home page rather than a carousel of images to rotate through
Should not have
• This is the existing website: http://www.plenvaro-example.org
We do not like the animation, the way the banner icons/titles bounce
Not simple enough, we don't like the functionality or how pages load so slowly
We do not like the logo centered - it should be at the left
The banner and its tabs should not be towards the right, we would like them to be centered, to go all the way across and to be below the logo

```html
<!DOCTYPE html>
<html lang="en">
<head>
<meta charset="utf-8">
<title>Plenvaro – Systems Knowledge Delivered</title>
<link rel="stylesheet" href="https://fonts.googleapis.com/css2?family=Lato:wght@300;400;700&display=swap">
<style>
:root{
  --red:#e8212b;
  --header:#16181a;
  --header-active:#0d0e0f;
  --ink:#2b2f33;
  --muted:#9aa0a8;
  --card-line:#e3e6ea;
  --welcome-bg:#fbf6f6;
  --footer:#2d3238;
  --footer-bar:#262a2f;
  --footer-text:#9ca3ab;
  --white:#fff;
}
*{box-sizing:border-box;margin:0;padding:0}
html,body{width:1200px;height:1126px;overflow:hidden}
body{font-family:'Lato',sans-serif;background:var(--white);position:relative;color:var(--ink)}
a{color:inherit;text-decoration:none}
ul{list-style:none}

/* header */
.site-header{position:absolute;left:0;top:0;width:1200px;height:72px;background:var(--header);z-index:3;border-bottom:1px solid #0a0b0c}
.brand{position:absolute;left:300px;top:24px;display:flex;align-items:center;gap:7px;color:var(--red);font-weight:700;font-size:15px;letter-spacing:3px}
.brand-mark{width:10px;height:10px;background:var(--red)}
.main-nav{position:absolute;left:492px;top:0;display:flex;height:72px}
.main-nav li{display:flex;flex-direction:column;align-items:center;justify-content:center;padding:0 11px;height:72px}
.main-nav .label{color:var(--white);font-size:9.5px;font-weight:700;letter-spacing:.2px}
.main-nav .sub{color:#7c8288;font-size:5.5px;margin-top:3px}
.main-nav .active{background:var(--header-active);padding:0 14px;border-bottom:1px solid var(--red)}
.main-nav .active .label{color:var(--red)}

/* hero */
.hero{position:absolute;left:0;top:72px;width:1200px;height:401px;overflow:hidden}
.hero-photo{position:absolute;inset:0;background:
  radial-gradient(ellipse 38% 55% at 50% 30%,#dfe7ec 0%,#8ea5b4 35%,transparent 70%),
  linear-gradient(90deg,#0d1d26 0%,#28414f 22%,#3e5a6b 50%,#1f3543 78%,#0b1820 100%);}
.hero-shade{position:absolute;inset:0;background:linear-gradient(180deg,rgba(0,0,0,0) 40%,rgba(0,0,0,.75) 100%)}
.hero-title{position:absolute;left:0;width:1200px;top:236px;text-align:center;color:var(--red);font-weight:300;font-size:38px;letter-spacing:-.3px;padding-left:10px}
.hero-text{position:absolute;left:385px;width:440px;top:287px;text-align:center;color:#e6e9ec;font-size:8.5px;line-height:15px}
.hero-wave{position:absolute;left:0;bottom:0}

/* services */
.services{position:absolute;left:0;top:473px;width:1200px;height:226px;background:var(--white)}
.service-card{position:absolute;top:58px;width:187px;height:126px;border:1px solid var(--card-line);border-top:2px solid var(--card-line);text-align:center}
.service-card .hex{position:absolute;left:68px;top:-30px}
.service-card h3{margin-top:40px;font-size:10px;font-weight:400;color:var(--ink)}
.service-card p{margin-top:8px;font-size:7.5px;line-height:12.5px;color:var(--muted)}
.btn{display:inline-block;background:var(--ink);color:var(--white);font-size:7px;padding:0 9px;height:18px;line-height:18px;border-radius:2px}
.btn-red{background:var(--red)}
.service-card .btn{position:absolute;left:70px;top:117px;width:50px;padding:0}

/* welcome */
.welcome{position:absolute;left:0;top:699px;width:1200px;height:244px;background:var(--welcome-bg)}
.welcome h2,.news h2{font-size:12px;font-weight:400;color:var(--ink);text-transform:uppercase}
.welcome-intro{position:absolute;left:308px;top:32px;width:375px}
.welcome-intro p{margin-top:10px;font-size:7.6px;line-height:12.6px;color:var(--muted)}
.welcome-intro p + p{margin-top:13px}
.welcome-intro .btn{margin-top:12px}
.news{position:absolute;left:707px;top:31px;width:200px}
.news-item{display:flex;gap:9px;margin-top:13px}
.news-item:first-of-type{margin-top:13px}
.news-item + .news-item{margin-top:19px}
.news-thumb{width:34px;height:34px;flex:none}
.news-item p{font-size:7.6px;line-height:12.5px;color:var(--muted)}
.news-item time{display:block;font-size:6.8px;color:#555b62;margin-top:1px}

/* footer */
.site-footer{position:absolute;left:0;top:943px;width:1200px;height:144px;background:var(--footer);color:var(--footer-text)}
.footer-brand{position:absolute;left:320px;top:60px;display:flex;align-items:center;gap:8px;color:var(--white);font-weight:700;font-size:16px;letter-spacing:3.5px}
.footer-brand .brand-mark{background:var(--white)}
.footer-col{position:absolute;top:35px}
.footer-col h4{color:var(--white);font-size:9.5px;font-weight:700}
.footer-nav{left:495px}
.footer-nav li{font-size:8px;margin-top:10px}
.footer-nav li::before{content:"›";margin-right:6px}
.newsletter{left:600px;width:165px}
.newsletter p{font-size:7.8px;line-height:13px;margin-top:10px}
.subscribe{display:flex;margin-top:13px;height:22px}
.subscribe .field{flex:1;background:#1f2327;color:#c5cad0;font-size:7.8px;line-height:22px;padding-left:8px}
.subscribe .btn{background:var(--red);height:22px;line-height:22px;border-radius:0;font-size:8px;padding:0 9px}
.contact{left:790px;width:150px}
.contact li{display:flex;gap:9px;font-size:8px;line-height:12.5px;margin-top:7px}
.contact li:first-child{margin-top:12px}
.contact svg{flex:none;margin-top:1px}
.footer-bar{position:absolute;left:0;top:1087px;width:1200px;height:39px;background:var(--footer-bar);color:#868d95;font-size:7px}
.footer-bar .copy{position:absolute;left:303px;top:16px}
.footer-bar .legal{position:absolute;right:324px;top:16px}
</style>
</head>
<body>

<header class="site-header">
  <a class="brand" href="#"><span class="brand-mark"></span>PLENVARO</a>
  <ul class="main-nav">
    <li class="active"><span class="label">HOME</span><span class="sub">Start here</span></li>
    <li><span class="label">ABOUT</span><span class="sub">Know us</span></li>
    <li><span class="label">SERVICES</span><span class="sub">We have</span></li>
    <li><span class="label">BUSINESS UNITS</span><span class="sub">The work</span></li>
    <li><span class="label">LOCATIONS</span><span class="sub">Where We Are</span></li>
    <li><span class="label">CONTACT</span><span class="sub">Get in touch</span></li>
  </ul>
</header>

<section class="hero">
  <div class="hero-photo" role="img" aria-label="Upward view of glass office towers against a pale sky"></div>
  <div class="hero-shade"></div>
  <h1 class="hero-title">Systems Knowledge Delivered</h1>
  <p class="hero-text">Plenvaro recognizes the middle east and greater asia regions are economic growth markets with developing infra-structure projects requiring specialist systems and technical expertise. accordingly, plenvaro has evolved its pres-ence in the regions to meet client demands and expectations.</p>
  <svg class="hero-wave" width="1200" height="30" viewBox="0 0 1200 30">
    <path d="M0 30 L480 30 C530 30 550 2 600 2 C650 2 670 30 720 30 L1200 30 Z" fill="#fff"/>
    <path d="M480 30 C530 30 550 2 600 2 C650 2 670 30 720 30" fill="none" stroke="#2f5d9a" stroke-width="1"/>
    <path d="M596 17 L600 21 L604 17" fill="none" stroke="#3a6fb0" stroke-width="1.3"/>
  </svg>
</section>

<section class="services">
  <article class="service-card" style="left:307px">
    <svg class="hex" width="50" height="56" viewBox="0 0 50 56"><path d="M25 1 L48 14 L48 42 L25 55 L2 42 L2 14 Z" fill="#2b2f33" stroke="#dfe3e7" stroke-width="3"/><rect x="14" y="24" width="16" height="8" rx="2" fill="#fff"/><rect x="17" y="20" width="10" height="5" rx="1.5" fill="#fff"/><rect x="22" y="29" width="14" height="7" rx="2" fill="#fff" stroke="#2b2f33"/><circle cx="17" cy="33" r="1.6" fill="#2b2f33"/><circle cx="33" cy="36" r="1.6" fill="#2b2f33"/></svg>
    <h3>Transportation</h3>
    <p>Fusce gravida tortor felis<br>Ac dictum risus sagittis id morbi posu<br>justo eleifend libero ultricies</p>
    <a class="btn btn-red" href="#">read more</a>
  </article>
  <article class="service-card" style="left:507px">
    <svg class="hex" width="50" height="56" viewBox="0 0 50 56"><path d="M25 1 L48 14 L48 42 L25 55 L2 42 L2 14 Z" fill="#2b2f33" stroke="#dfe3e7" stroke-width="3"/><path d="M16 24 L25 19 L34 24 Z" fill="#fff"/><rect x="17" y="25" width="2" height="8" fill="#fff"/><rect x="21" y="25" width="2" height="8" fill="#fff"/><rect x="27" y="25" width="2" height="8" fill="#fff"/><rect x="31" y="25" width="2" height="8" fill="#fff"/><rect x="15" y="34" width="20" height="2" fill="#fff"/></svg>
    <h3>Government</h3>
    <p>Fusce gravida tortor felis<br>Ac dictum risus sagittis id morbi posu<br>justo eleifend libero ultricies</p>
    <a class="btn" href="#">read more</a>
  </article>
  <article class="service-card" style="left:706px">
    <svg class="hex" width="50" height="56" viewBox="0 0 50 56"><path d="M25 1 L48 14 L48 42 L25 55 L2 42 L2 14 Z" fill="#2b2f33" stroke="#dfe3e7" stroke-width="3"/><rect x="19" y="18" width="12" height="19" fill="#fff"/><g fill="#2b2f33"><rect x="21" y="21" width="3" height="2"/><rect x="26" y="21" width="3" height="2"/><rect x="21" y="25" width="3" height="2"/><rect x="26" y="25" width="3" height="2"/><rect x="21" y="29" width="3" height="2"/><rect x="26" y="29" width="3" height="2"/><rect x="23.5" y="33" width="3" height="4"/></g></svg>
    <h3>Commercial Sectors</h3>
    <p>Fusce gravida tortor felis<br>Ac dictum risus sagittis id morbi posu<br>justo eleifend libero ultricies</p>
    <a class="btn" href="#">read more</a>
  </article>
</section>

<section class="welcome">
  <div class="welcome-intro">
    <h2>Welcome to Plenvaro</h2>
    <p>Plenvaro specializes in delivering quality professional services and technical projects that support larger business goals. systems are tools that support a greater business function and need. we understand that most technical projects are conceptualized to support a larger vision with actual business goals in mind and ensure that all of our professional and certified expertise is included in our professional services to meet those goals.</p>
    <p>Our ultimate goal is to provide quality, technical and professional services on projects of any scale and/or complexity, from conception through to completion. our philosophy is simple; stick to what you are good at and be the best at it.</p>
    <a class="btn" href="#">read more</a>
  </div>
  <div class="news">
    <h2>Recent Blog/News</h2>
    <div class="news-item">
      <div class="news-thumb" role="img" aria-label="Photo of two colleagues talking" style="background:linear-gradient(135deg,#5b6670,#2c333a)"></div>
      <div><p>Fusce gravida tortor felis, ac dictum risus sagittis. Fusce gravida tortor felis.</p><time>October 15, 2013</time></div>
    </div>
    <div class="news-item">
      <div class="news-thumb" role="img" aria-label="Photo of a businesswoman" style="background:linear-gradient(135deg,#d9cfc8,#8a7a70)"></div>
      <div><p>Fusce gravida tortor felis, ac dictum risus sagittis. Fusce gravida tortor felis.</p><time>October 15, 2013</time></div>
    </div>
    <div class="news-item">
      <div class="news-thumb" role="img" aria-label="Photo of hands using a tablet" style="background:linear-gradient(135deg,#aebbc6,#3c4a57)"></div>
      <div><p>Fusce gravida tortor felis, ac dictum risus sagittis. Fusce gravida tortor felis.</p><time>October 15, 2013</time></div>
    </div>
  </div>
</section>

<footer class="site-footer">
  <a class="footer-brand" href="#"><span class="brand-mark"></span>PLENVARO</a>
  <div class="footer-col footer-nav">
    <h4>Navigation</h4>
    <ul><li>Home</li><li>Services</li><li>About</li><li>Blog</li></ul>
  </div>
  <div class="footer-col newsletter">
    <h4>Newsletter</h4>
    <p>Ipsum dolor sit amet, teft consecte tur adipiscing elit ut eunt.</p>
    <div class="subscribe"><span class="field">Email Address</span><span class="btn">Subscribe</span></div>
  </div>
  <div class="footer-col contact">
    <h4>Contact Details</h4>
    <ul>
      <li><svg width="11" height="11" viewBox="0 0 12 12"><path d="M2.5 1 L4.5 1 L5.5 3.5 L4 4.6 C4.7 6 6 7.3 7.4 8 L8.5 6.5 L11 7.5 L11 9.5 C11 10.3 10.3 11 9.5 11 C5 11 1 7 1 2.5 C1 1.7 1.7 1 2.5 1Z" fill="#9ca3ab"/></svg>+1800-555-0147</li>
      <li><svg width="11" height="11" viewBox="0 0 12 12"><rect x="1" y="2.5" width="10" height="7" fill="none" stroke="#9ca3ab"/><path d="M1 2.5 L6 6.5 L11 2.5" fill="none" stroke="#9ca3ab"/></svg>info@plenvaro-mail.com</li>
      <li><svg width="11" height="12" viewBox="0 0 12 13"><path d="M6 1 C3.5 1 2 2.8 2 4.8 C2 7.5 6 12 6 12 C6 12 10 7.5 10 4.8 C10 2.8 8.5 1 6 1Z" fill="#9ca3ab"/><circle cx="6" cy="4.8" r="1.5" fill="#2d3238"/></svg>Your Address, Your Country<br>Your Zip Code</li>
    </ul>
  </div>
</footer>
<div class="footer-bar">
  <span class="copy">Copyright © 2014 - Plenvaro International. All Rights reserved</span>
  <span class="legal">Privacy Policy &nbsp;|&nbsp; Sitemap</span>
</div>

</body>
</html>
```